Create the design of Sitepelican (in photoshop or similar)

*edit* What we wanna see is a sketch of a first page, and then in the end 5 page designs, but the main page will be the big tasks other pages are just basically pop-ups or form. *edit*

We need a web design for our new startup Sitepelican in turn will be providing web pages to smaller business. So the purpose of the page is to clearly showcase the message in a web 3.0 fashion, good design looks but function should always be the main focus.Further more we are looking for a long term relationship with a good designer / design company that can help us design the future web sites for our customers as well.

We need you to understand web, not just design. You need to be up to date with how web looks and works, and how to make it as simple and easy to use as possible for the customer and at the same time good looking.

Please look at the PDF for full description of the project.

Colors and layout are free to choose, but we really like the kind of layout that forkglider.com has so feel free to be inspired by them.

We want all of the pages design, but the main/landing page will be the big part, the rest are small pages that will use the same design frame as the main page.

PS. We just want the design in photoshop or illustrator format, the website will then be built in page tidal by page tidal experts (let us know if you/company also possess this knowledge)

Target Market(s)

Small to medium sized business, mostly owner/entrepreneur driven companies.

Industry/Entity Type

Business

Font styles to use
Other font styles liked:
• Helvetica for the win

Requirements
Must have
• Great and simple design, a child should be able to understand the message and also enjoy reading it. Should be a funny website while still being professional, i.e. see postbadger.com for example.

```html
<!DOCTYPE html>
<html lang="en">
<head>
<meta charset="utf-8">
<title>Sitepelican – most convenient web ever</title>
<link rel="stylesheet" href="https://fonts.googleapis.com/css2?family=Roboto:wght@300;400&family=Montserrat:wght@400;500&family=PT+Sans+Narrow&display=swap">
<style>
  :root {
    --pink: #de426f;
    --yellow: #efd71a;
    --ink: #3b3a36;
    --olive: #5c5a4e;
    --body: #111111;
    --footer-bg: #dfdfdd;
    --footer-ink: #333333;
    --white: #ffffff;
    --divider: #8a8a8a;
  }
  * { box-sizing: border-box; margin: 0; padding: 0; }
  html, body { width: 1200px; height: 706px; overflow: hidden; background: var(--white); }
  .page { position: relative; width: 1200px; height: 706px; font-family: Arial, Helvetica, sans-serif; color: var(--ink); }

  /* header */
  .site-header { position: absolute; left: 0; top: 0; width: 1200px; height: 145px; }
  .brand { position: absolute; left: 183px; top: 48px; }
  .brand-name { font-family: "Roboto", Arial, sans-serif; font-weight: 300; font-size: 40px; line-height: 1; color: var(--olive); letter-spacing: -0.5px; }
  .brand-tagline { font-family: "Roboto", Arial, sans-serif; font-weight: 400; font-size: 16.5px; color: var(--olive); margin: 2px 0 0 14px; letter-spacing: 0.2px; }

  .utility { position: absolute; top: 14px; font-family: "Montserrat", Arial, sans-serif; font-size: 10px; color: var(--ink); }
  .utility-chat { left: 800px; width: 44px; text-align: center; }
  .utility-lang { left: 852px; width: 62px; text-align: center; padding-left: 6px; border-left: 1px dashed #bbbbbb; height: 48px; }
  .utility-label { display: block; margin-bottom: 8px; }
  .chat-button { display: inline-block; width: 35px; height: 21px; border-radius: 5px; background: #e0622e; }
  .lang-flag { display: inline-block; width: 20px; height: 20px; border-radius: 50%; margin: 0 2px; }
  .lang-sv { background: radial-gradient(circle, #f2c81a 0 35%, #1e63b0 36%); }
  .lang-en { background: radial-gradient(circle, #d22c3a 0 30%, #f2f2f2 31% 45%, #26337a 46%); }

  .quick-links { position: absolute; left: 948px; top: 41px; font-family: "Montserrat", Arial, sans-serif; font-size: 10.5px; color: var(--ink); }
  .quick-links .sep { margin: 0 5px; }
  .quick-links .order { color: var(--pink); }

  .main-nav { position: absolute; right: 186px; top: 92px; font-family: "Montserrat", Arial, sans-serif; font-size: 14px; color: var(--ink); }
  .main-nav .sep { margin: 0 8px; }

  /* hero */
  .hero { position: absolute; left: 0; top: 145px; width: 1200px; height: 250px; background: var(--pink); }
  .hero-title { position: absolute; left: 219px; top: 22px; font-family: "Roboto", Arial, sans-serif; font-weight: 300; color: var(--white); }
  .hero-title .lead { display: block; font-size: 30px; line-height: 1; }
  .hero-title .name { display: block; font-size: 49px; line-height: 1; margin-top: 14px; color: var(--yellow); letter-spacing: -0.5px; }
  .hero-points { position: absolute; left: 221px; top: 127px; list-style: none; font-family: "PT Sans Narrow", Arial, sans-serif; font-size: 19px; line-height: 22px; color: var(--white); }
  .hero-points li { position: relative; padding-left: 18px; margin-bottom: 9px; }
  .hero-points li::before { content: ""; position: absolute; left: 2px; top: 8px; width: 6px; height: 6px; border-radius: 50%; background: var(--white); }
  .hero-art { position: absolute; left: 638px; top: 28px; width: 194px; height: 195px; border-radius: 8px; background: linear-gradient(135deg, #f4d3dc, #e7758f); opacity: 0.8; }

  /* features */
  .feature-art { position: absolute; }
  .art-money { left: 128px; top: 463px; width: 132px; height: 112px; border-radius: 10px; background: linear-gradient(180deg, #dcc39a 0%, #8fa87a 100%); }
  .art-mood { left: 635px; top: 472px; width: 102px; height: 102px; border-radius: 50%; background: radial-gradient(circle at 40% 35%, #fde36a, #f3a511); border: 1px solid #d98a10; }
  .feature { position: absolute; top: 458px; width: 260px; }
  .feature-cost { left: 286px; }
  .feature-support { left: 759px; }
  .feature-title { font-family: "Montserrat", Arial, sans-serif; font-weight: 400; font-size: 18px; color: var(--ink); margin-bottom: 6px; letter-spacing: 0.2px; }
  .feature-text { font-size: 10.3px; line-height: 17px; color: var(--body); text-align: justify; text-align-last: justify; height: 85px; overflow: hidden; }
  .feature-divider { position: absolute; left: 600px; top: 469px; height: 100px; border-left: 1px dotted var(--divider); }

  /* footer */
  .site-footer { position: absolute; left: 0; top: 631px; width: 1200px; height: 75px; background: var(--footer-bg); text-align: center; font-size: 10.3px; color: var(--footer-ink); }
  .site-footer .copyright { margin-top: 25px; }
  .site-footer .footer-links { margin-top: 11px; }
  .site-footer .sep { margin: 0 5px; }
</style>
</head>
<body>
<div class="page">
  <header class="site-header">
    <div class="brand">
      <div class="brand-name">Sitepelican</div>
      <div class="brand-tagline">most convenient web ever</div>
    </div>

    <div class="utility utility-chat">
      <span class="utility-label">Chat</span>
      <span class="chat-button" role="img" aria-label="Live chat button"></span>
    </div>
    <div class="utility utility-lang">
      <span class="utility-label">Language</span>
      <span class="lang-flag lang-sv" role="img" aria-label="Swedish"></span><span class="lang-flag lang-en" role="img" aria-label="English"></span>
    </div>

    <nav class="quick-links"><span>FAQ</span><span class="sep">|</span><span class="order">Order</span></nav>

    <nav class="main-nav">
      <span>Home</span><span class="sep">|</span><span>How it works</span><span class="sep">|</span><span>About</span><span class="sep">|</span><span>Contact</span>
    </nav>
  </header>

  <section class="hero">
    <h1 class="hero-title">
      <span class="lead">What is</span>
      <span class="name">Sitepelican?</span>
    </h1>
    <ul class="hero-points">
      <li>Your website on subscription autopilot with<br>free unlimited support and updates.</li>
      <li>Delivered by professionals.</li>
    </ul>
    <div class="hero-art" role="img" aria-label="White rocket illustration with a globe window and a yellow question mark"></div>
  </section>

  <section class="features">
    <div class="feature-art art-money" role="img" aria-label="Illustration of a money bag on a pile of banknotes"></div>
    <article class="feature feature-cost">
      <h2 class="feature-title">What does it cost?</h2>
      <p class="feature-text">Lorem ipsum dolor sit amet, consectetur adipiscing elit. Sed at ante. Mauris eleifend, quam a vulputate dictum, massa quam dapibus leo, eget vulputate orci purus ut lorem. In fringilla mi in ligula. Pellentesque aliquam quam vel dolor. Nunc adipiscing. Sed quam odio,</p>
    </article>

    <div class="feature-divider"></div>

    <div class="feature-art art-mood" role="img" aria-label="Illustration of an unhappy yellow emoticon"></div>
    <article class="feature feature-support">
      <h2 class="feature-title">If you are unhappy?</h2>
      <p class="feature-text">Lorem ipsum dolor sit amet, consectetur adipiscing elit. Sed at ante. Mauris eleifend, quam a vulputate dictum, massa quam dapibus leo, eget vulputate orci purus ut lorem. In fringilla mi in ligula. Pellentesque aliquam quam vel dolor. Nunc adipiscing. Sed quam odio,</p>
    </article>
  </section>

  <footer class="site-footer">
    <p class="copyright">Copyright 2014 Sitepelican</p>
    <p class="footer-links"><span>Contact Us</span><span class="sep">|</span><span>Terms and Conditions</span></p>
  </footer>
</div>
</body>
</html>
```